Dinewell - Tablet App Design Project

I have a Tablet app that serves as a restaurant reservation system. The design that i currently have is very basic apple design. I am looking for it to have a much more professional appeal.

Please review the attached document which contains all of the screen shots for the app.
Updates

This Project has now been Guaranteed.  I look forward to reviewing your designs.

Brent

Reason: I am extending my deadline because i just changed this contest to guaranteed and have received a ton more "acceptances" because of it and I want to give those designers a chance to submit a design.

Target Market(s)

restaurant owners

Industry/Entity Type

Restaurant

Requirements
Must have
• On the seating chart i am changing the feature that shows the tables highlighted and instead would like that replace with a badge. So the list of wait staff across the top of the seating chart would instead have a number next to their name and would correspond with the badge on the table to determine their section.

So for example:
Ada would have a number 1 in front of her name and tables 18, 19, 20, and 31 would have a little badge in the upper right hand corner with the number "1" inside the badge.
Uma would have a number 2 in front of her name and tables 6, 7, and 11 would have a little badge in the upper right hand corner with the number " 2" inside the badge.
Nora would have a number 3 in front of her name and tables 12, 13, 27, 28, 29, and 30 would have a little badge in the upper right hand corner with the number " 3" inside the badge.

The names on the top will all be ONE color

Also, i would like an icon developed to replace the "C" you see next to some of the people's name in the reservation and waitlist slots. Also, i would like a better looking "check mark".

```html
<!DOCTYPE html>
<html lang="en">
<head>
<meta charset="utf-8">
<title>Dinewell – Reservations</title>
<link href="https://fonts.googleapis.com/css2?family=Open+Sans:ital,wght@0,300;0,400;0,600;0,700;1,400&family=Roboto+Condensed:wght@400;700&display=swap" rel="stylesheet">
<style>
:root{
  --page:#d9dbe0;
  --statusbar:#000;
  --toolbar-top:#f4f5f7;
  --toolbar-bot:#c9ccd2;
  --btn-top:#9ea4ad;
  --btn-bot:#6c727c;
  --btn-border:#555b64;
  --ink:#1d1d1f;
  --muted:#6a6a6a;
  --label:#555;
  --blue:#1b8fe0;
  --blue-dark:#0d6fc0;
  --red:#e0262e;
  --green:#6cc04a;
  --rule:#cfd2d6;
  --panel:#f1f1f1;
  --panel-stripe:#8d9096;
  --board:#5e6273;
  --card:#fff;
  --card-head:#eceef1;
}
*{box-sizing:border-box;margin:0;padding:0}
html,body{width:1200px;height:1000px;overflow:hidden}
body{background:var(--page);font-family:"Open Sans",Arial,sans-serif;color:var(--ink)}
.screen{position:absolute;left:0;top:50px;width:1024px;height:768px;transform:scale(1.171875);transform-origin:0 0;background:var(--board);overflow:hidden}

.status-bar{height:20px;background:var(--statusbar);color:#fff;font-size:12px;font-weight:600;display:flex;align-items:center;justify-content:space-between;padding:0 6px;position:relative}
.status-bar .clock{position:absolute;left:50%;transform:translateX(-50%)}
.status-bar .left,.status-bar .right{display:flex;align-items:center;gap:5px}

.toolbar{height:42px;background:linear-gradient(var(--toolbar-top),var(--toolbar-bot));border-bottom:1px solid #9da1a8;display:flex;align-items:center;padding:0 7px;position:relative}
.btn{height:29px;padding:0 10px;border-radius:5px;border:1px solid var(--btn-border);background:linear-gradient(var(--btn-top),var(--btn-bot));color:#fff;font-size:12px;font-weight:700;display:flex;align-items:center;margin-right:7px;box-shadow:inset 0 1px 0 rgba(255,255,255,.35)}
.btn.disabled{background:linear-gradient(#d9dbde,#c4c7cb);border-color:#b4b7bb;color:#eef0f2}
.toolbar .right{margin-left:auto;display:flex}
.toolbar .right .btn:last-child{margin-right:0}
.brand{position:absolute;left:50%;top:4px;transform:translateX(-50%);font-size:28px;font-weight:300;color:var(--blue);letter-spacing:-.5px}

.stats{height:52px;background:#fff;display:flex;border-bottom:1px solid var(--rule)}
.stat{border-left:1px solid var(--rule);padding:6px 0 0 12px;flex:none}
.stat:first-child{border-left:0;width:128px}
.stat:nth-child(2){width:180px}
.stat:nth-child(3){width:182px}
.stat:nth-child(4){width:180px}
.stat:nth-child(5){width:182px}
.stat:nth-child(6){flex:1}
.stat .label{font-family:"Roboto Condensed","Arial Narrow",sans-serif;font-size:12.5px;font-weight:700;color:var(--label);letter-spacing:.2px}
.stat .value{font-size:18px;color:var(--blue);line-height:22px}
.stat .value small{font-size:13px}
.now .time{font-size:16px;line-height:18px;margin-top:1px}
.now .date{font-size:15px;color:var(--muted)}

.main{display:flex;height:654px}
.waitlist{width:333px;background:var(--panel);border-left:6px solid var(--panel-stripe);border-right:1px solid #c8c8c8}
.wl-head{height:68px;display:flex;align-items:center;padding:0 10px 0 14px;border-bottom:1px solid var(--rule)}
.wl-head h2{font-weight:400;font-size:25px;color:#333;margin-left:8px;letter-spacing:-.3px}
.add-party{margin-left:auto;background:linear-gradient(#3ca6f0,var(--blue-dark));color:#fff;font-size:11px;font-weight:700;padding:6px 9px;border-radius:5px;border:1px solid #0b5da3}
.party{height:54px;border-bottom:1px solid var(--rule);display:flex;align-items:center;padding:0 10px 0 13px}
.party .who{flex:1;line-height:14px}
.party .name{font-size:12.5px;font-weight:600}
.party .size{font-size:10.5px;font-weight:600;color:#333}
.party .note{font-size:10.5px;font-style:italic;color:#555}
.party .wait{font-size:12px;display:flex;align-items:center;gap:6px}
.party .wait b{font-weight:700}
.party .wait.late{color:var(--red)}

.board{flex:1;display:flex;gap:14px;padding:16px 0 0 14px}
.col{width:323px}
.slot{background:var(--card);border-radius:4px;margin-bottom:11px;overflow:hidden;box-shadow:0 1px 2px rgba(0,0,0,.3)}
.slot-head{height:28px;background:var(--card-head);display:flex;align-items:center;border-bottom:1px solid #b9bec4}
.time-tab{width:86px;height:100%;background:linear-gradient(#3aa3ee,var(--blue-dark));color:#fff;font-size:15px;font-weight:600;display:flex;align-items:center;padding-left:10px}
.time-tab small{font-size:10px;margin-left:3px}
.count{font-size:15px;color:var(--blue-dark);margin-left:14px}
.count.full{color:var(--red);font-weight:700}
.plus{margin-left:auto;margin-right:7px;width:20px;height:20px;border-radius:50%;background:linear-gradient(#3aa3ee,var(--blue-dark));border:1px solid #0b5da3;color:#fff;font-weight:700;font-size:17px;line-height:17px;text-align:center}
.res{height:40px;display:flex;align-items:center;border-bottom:1px solid #e1e3e6}
.res:last-child{border-bottom:0}
.res .who{flex:1;padding-left:9px;line-height:14px;min-width:0}
.res .name{font-size:13px;font-weight:600}
.res .note{font-size:10.5px;font-style:italic;color:#555;white-space:nowrap}
.res .icons{display:flex;gap:7px;align-items:center;margin-right:8px}
.res .size{width:20px;font-size:13px;text-align:right;margin-right:6px}
.res .table{width:31px;height:100%;border-left:1px solid #e1e3e6;display:flex;align-items:center;justify-content:center}
.table-no{width:17px;height:16px;border:1px solid #555;font-size:10px;line-height:14px;text-align:center}
</style>
</head>
<body>
<svg width="0" height="0" style="position:absolute">
  <defs>
    <symbol id="i-note" viewBox="0 0 12 12"><rect x=".5" y=".5" width="11" height="11" rx="1.5" fill="#e8f6df" stroke="#6cc04a"/><path d="M3 3.5h6M3 6h6M3 8.5h6" stroke="#6cc04a" stroke-width="1.1"/></symbol>
    <symbol id="i-host" viewBox="0 0 16 12"><path d="M5 4a3 3 0 0 1 6 0z" fill="#6cc04a"/><rect x="7.2" y="0" width="1.6" height="1.6" rx=".8" fill="#6cc04a"/><rect x="3" y="4.6" width="10" height="1.4" rx=".7" fill="#6cc04a"/><path d="M8 6.5v2.5M3 12c0-2 2-3 5-3s5 1 5 3z" fill="#6cc04a" stroke="#6cc04a" stroke-width=".6"/></symbol>
  </defs>
</svg>

<div class="screen">
  <div class="status-bar">
    <span class="left">Tablet
      <svg width="14" height="10" viewBox="0 0 14 10"><path d="M1 3.5a8.5 8.5 0 0 1 12 0M3 5.8a5.5 5.5 0 0 1 8 0M5 8a2.5 2.5 0 0 1 4 0" fill="none" stroke="#fff" stroke-width="1.5"/></svg></span>
    <span class="clock">2:17 PM</span>
    <span class="right">Not Charging
      <svg width="24" height="11" viewBox="0 0 24 11"><rect x=".5" y=".5" width="20" height="10" rx="2" fill="none" stroke="#fff"/><rect x="2" y="2" width="14" height="7" fill="#fff"/><rect x="21" y="3.5" width="2" height="4" fill="#fff"/></svg></span>
  </div>

  <header class="toolbar">
    <span class="btn">Seating Chart</span>
    <span class="btn">Specials</span>
    <span class="btn">Staff Notes</span>
    <span class="brand">Dinewell</span>
    <div class="right">
      <span class="btn">Calendar</span>
      <span class="btn disabled">Management</span>
    </div>
  </header>

  <section class="stats">
    <div class="stat now"><div class="time">2:17 PM</div><div class="date">Mon Sep 10</div></div>
    <div class="stat"><div class="label">AVG WAIT TIME</div><div class="value">25 <small>min</small></div></div>
    <div class="stat"><div class="label">OPEN TABLES</div><div class="value">66</div></div>
    <div class="stat"><div class="label">CHECKED IN</div><div class="value">14 <small>Groups</small> &nbsp;56 <small>People</small></div></div>
    <div class="stat"><div class="label">CURRENTLY SEATED</div><div class="value">11/296</div></div>
    <div class="stat"><div class="label">OPEN RESERVATIONS</div><div class="value">370 <small>People</small></div></div>
  </section>

  <div class="main">
    <aside class="waitlist">
      <div class="wl-head">
        <svg width="16" height="22" viewBox="0 0 16 22"><path d="M1 1h14M1 21h14M3 1c0 6 4 7 5 10-1 3-5 4-5 10M13 1c0 6-4 7-5 10 1 3 5 4 5 10" fill="none" stroke="#666" stroke-width="1.6"/><path d="M4.5 19c1-2 2.5-3 3.5-3s2.5 1 3.5 3z" fill="#666"/></svg>
        <h2>WAIT LIST</h2>
        <span class="add-party">ADD A PARTY</span>
      </div>
      <div class="party"><div class="who"><div class="name">Clara Whitby</div><div class="size">PARTY OF 4</div><div class="note">I would like a booth in the corner</div></div><div class="wait late"><svg width="12" height="12"><use href="#i-note"/></svg><span><b>5m</b> (2:02 PM)</span></div></div>
      <div class="party"><div class="who"><div class="name">Brent Hollis</div><div class="size">PARTY OF 2</div><div class="note">Birthday celebration</div></div><div class="wait late"><svg width="12" height="12"><use href="#i-note"/></svg><span><b>5m</b> (2:02 PM)</span></div></div>
      <div class="party"><div class="who"><div class="name">Rhea Lund</div><div class="size">PARTY OF 4</div><div class="note">One person needs gluten free food</div></div><div class="wait"><svg width="12" height="12"><use href="#i-note"/></svg><span><b>25m</b> (2:22 PM)</span></div></div>
      <div class="party"><div class="who"><div class="name">Mirela Castor</div><div class="size">PARTY OF 3</div></div><div class="wait"><span><b>25m</b> (2:23 PM)</span></div></div>
      <div class="party"><div class="who"><div class="name">Selin Arvani</div><div class="size">PARTY OF 4</div><div class="note">I would like a booth in the corner</div></div><div class="wait"><svg width="12" height="12"><use href="#i-note"/></svg><span><b>30m</b> (2:28 PM)</span></div></div>
      <div class="party"><div class="who"><div class="name">Odette Varga</div><div class="size">PARTY OF 6</div></div><div class="wait"><span><b>30m</b> (2:28 PM)</span></div></div>
      <div class="party"><div class="who"><div class="name">Petra Solis</div><div class="size">PARTY OF 6</div><div class="note">I would like a booth in the corner</div></div><div class="wait"><svg width="12" height="12"><use href="#i-note"/></svg><span><b>30m</b> (2:28 PM)</span></div></div>
      <div class="party"><div class="who"><div class="name">Lorna Quaid</div><div class="size">PARTY OF 4</div></div><div class="wait late"><span><b>15m</b> (2:14PM)</span></div></div>
      <div class="party"><div class="who"><div class="name">Felix Dorran</div><div class="size">PARTY OF 5</div><div class="note">I would like a booth in the corner</div></div><div class="wait"><svg width="12" height="12"><use href="#i-note"/></svg><span><b>40m</b> (2:39 PM)</span></div></div>
    </aside>

    <section class="board">
      <div class="col">
        <div class="slot">
          <div class="slot-head"><span class="time-tab">12:00<small>PM</small></span><span class="count">19/22</span><span class="plus">+</span></div>
          <div class="res"><div class="who"><div class="name">Owen Pratt</div><div class="note">I would like a booth in the corner</div></div><span class="icons"><svg width="16" height="12"><use href="#i-host"/></svg></span><span class="size">4</span><span class="table"><span class="table-no">11</span></span></div>
          <div class="res"><div class="who"><div class="name">Ada Renko</div></div><span class="icons"><svg width="16" height="12"><use href="#i-host"/></svg><svg width="12" height="12"><use href="#i-note"/></svg></span><span class="size">3</span><span class="table"></span></div>
          <div class="res"><div class="who"><div class="name">Hugo Marsh</div><div class="note">Patio table if available</div></div><span class="size">2</span><span class="table"><span class="table-no">1</span></span></div>
        </div>
        <div class="slot">
          <div class="slot-head"><span class="time-tab">12:15<small>PM</small></span><span class="count full">FULL</span><span class="plus">+</span></div>
          <div class="res"><div class="who"><div class="name">Ivan Crole</div></div><span class="icons"><svg width="16" height="12"><use href="#i-host"/></svg><svg width="12" height="12"><use href="#i-note"/></svg></span><span class="size">4</span><span class="table"></span></div>
          <div class="res"><div class="who"><div class="name">Milo Garret</div><div class="note">Birthday celebration</div></div><span class="icons"><svg width="16" height="12"><use href="#i-host"/></svg></span><span class="size">5</span><span class="table"><span class="table-no">12</span></span></div>
          <div class="res"><div class="who"><div class="name">Theo Wrenn</div><div class="note">One person needs gluten free food</div></div><span class="icons"><svg width="16" height="12"><use href="#i-host"/></svg></span><span class="size">2</span><span class="table"></span></div>
          <div class="res"><div class="who"><div class="name">Nils Parry</div><div class="note">Patio table if available</div></div><span class="size">4</span><span class="table"></span></div>
        </div>
        <div class="slot">
          <div class="slot-head"><span class="time-tab">12:30<small>PM</small></span><span class="count">12/20</span><span class="plus">+</span></div>
          <div class="res"><div class="who"><div class="name">Greta Holm</div></div><span class="icons"><svg width="16" height="12"><use href="#i-host"/></svg></span><span class="size">4</span><span class="table"></span></div>
          <div class="res"><div class="who"><div class="name">Vera Lomax</div></div><span class="icons"><svg width="16" height="12"><use href="#i-host"/></svg></span><span class="size">5</span><span class="table"></span></div>
          <div class="res"><div class="who"><div class="name">Damon Fitch</div><div class="note">Patio table if available</div></div><span class="icons"><svg width="12" height="12"><use href="#i-note"/></svg></span><span class="size">3</span><span class="table"></span></div>
        </div>
        <div class="slot">
          <div class="slot-head"><span class="time-tab">12:45<small>PM</small></span><span class="count">7/20</span><span class="plus">+</span></div>
          <div class="res"><div class="who"><div class="name">Ross Ellery</div></div><span class="size">2</span><span class="table"></span></div>
          <div class="res"><div class="who"><div class="name">Karim Osei</div></div><span class="icons"><svg width="12" height="12"><use href="#i-note"/></svg></span><span class="size">4</span><span class="table"></span></div>
        </div>
      </div>

      <div class="col">
        <div class="slot">
          <div class="slot-head"><span class="time-tab">1:00<small>PM</small></span><span class="count full">FULL</span><span class="plus">+</span></div>
          <div class="res"><div class="who"><div class="name">Leo Bramley</div><div class="note">Quiet table in back</div></div><span class="icons"><svg width="12" height="12"><use href="#i-note"/></svg></span><span class="size">2</span><span class="table"></span></div>
          <div class="res"><div class="who"><div class="name">Vesna Larrow</div><div class="note">Birthday celebration</div></div><span class="size">4</span><span class="table"><span class="table-no">12</span></span></div>
          <div class="res"><div class="who"><div class="name">Carys Penn</div><div class="note">booth please</div></div><span class="icons"><svg width="12" height="12"><use href="#i-note"/></svg></span><span class="size">3</span><span class="table"></span></div>
          <div class="res"><div class="who"><div class="name">Mara Tolley</div><div class="note">Patio table if available</div></div><span class="size">4</span><span class="table"></span></div>
        </div>
        <div class="slot">
          <div class="slot-head"><span class="time-tab">1:15<small>PM</small></span><span class="count">17/20</span><span class="plus">+</span></div>
          <div class="res"><div class="who"><div class="name">Ada Pellin</div></div><span class="icons"><svg width="16" height="12"><use href="#i-host"/></svg></span><span class="size">5</span><span class="table"></span></div>
          <div class="res"><div class="who"><div class="name">Jonah Keel</div><div class="note">Business meeting</div></div><span class="icons"><svg width="16" height="12"><use href="#i-host"/></svg></span><span class="size">8</span><span class="table"></span></div>
          <div class="res"><div class="who"><div class="name">Silas Orme</div></div><span class="icons"><svg width="12" height="12"><use href="#i-note"/></svg></span><span class="size">4</span><span class="table"></span></div>
        </div>
        <div class="slot">
          <div class="slot-head"><span class="time-tab">1:30<small>PM</small></span><span class="count full">FULL</span><span class="plus">+</span></div>
          <div class="res"><div class="who"><div class="name">Bram Tullo</div></div><span class="size">6</span><span class="table"></span></div>
          <div class="res"><div class="who"><div class="name">Dean Kersey</div><div class="note">Patio Please</div></div><span class="size">2</span><span class="table"></span></div>
          <div class="res"><div class="who"><div class="name">Noemi Straka</div></div><span class="size">6</span><span class="table"></span></div>
          <div class="res"><div class="who"><div class="name">Eli Gantner</div></div><span class="size">2</span><span class="table"></span></div>
        </div>
        <div class="slot">
          <div class="slot-head"><span class="time-tab">1:45<small>PM</small></span><span class="count">7/20</span><span class="plus">+</span></div>
          <div class="res"><div class="who"><div class="name">Ross Ellery</div></div><span class="icons"><svg width="12" height="12"><use href="#i-note"/></svg></span><span class="size">4</span><span class="table"></span></div>
        </div>
      </div>
    </section>
  </div>
</div>
</body>
</html>
```